Stationery Project with Logo Design

We need stationery & logo design for a new small boutique marketing company based in Perth Western Australia. The company is called Blue Harbor Marketing.

We offer marketing services to small-to-medium business.

We would like to see designs strong & innovative designs and should use red as one of the colours.

The final design should communicate innovation and fun.

Target Market(s)

Small to medium business owners between 20 - 50 years

Industry/Entity Type

Business

Logo Text

```html
<!DOCTYPE html>
<html lang="en">
<head>
<meta charset="utf-8">
<title>Blue Harbor Marketing – Letterhead</title>
<link rel="stylesheet" href="https://fonts.googleapis.com/css2?family=Montserrat:wght@600&display=swap">
<style>
  :root {
    --brand-red: #c20e22;
    --band-tint: #dd7480;
    --diamond-tint: #fbf1f2;
    --paper: #ffffff;
  }
  html, body {
    margin: 0;
    padding: 0;
    overflow: hidden;
    background: var(--paper);
  }
  .letterhead {
    position: relative;
    width: 849px;
    height: 1200px;
    overflow: hidden;
    background: var(--paper);
  }
  .letterhead__backdrop {
    position: absolute;
    inset: 0;
    width: 849px;
    height: 1200px;
  }
  .diamond { fill: var(--diamond-tint); }
  .footer-band__tint { fill: var(--band-tint); }
  .footer-band__main { fill: var(--brand-red); }

  .brand {
    position: absolute;
    top: 72px;
    left: 0;
    width: 849px;
    display: flex;
    justify-content: center;
    align-items: center;
    gap: 12px;
  }
  .brand__mark {
    width: 18px;
    height: 18px;
    background: var(--brand-red);
  }
  .brand__name {
    margin: 0;
    font-family: "Montserrat", Arial, sans-serif;
    font-weight: 600;
    font-size: 26px;
    line-height: 1;
    color: var(--brand-red);
    white-space: nowrap;
  }
</style>
</head>
<body>
  <main class="letterhead">
    <svg class="letterhead__backdrop" viewBox="0 0 827 1169" preserveAspectRatio="none" aria-hidden="true">
      <g class="diamond-stack">
        <polygon class="diamond" points="0,510 105,630 0,750"/>
        <polygon class="diamond" points="108,665 235,808 110,952 -17,808"/>
        <polygon class="diamond" points="0,875 105,995 0,1115"/>
        <polygon class="diamond" points="207,915 355,1087 60,1087"/>
      </g>
      <g class="footer-band">
        <rect class="footer-band__tint" x="0" y="1087" width="827" height="14"/>
        <rect class="footer-band__main" x="0" y="1101" width="827" height="68"/>
      </g>
    </svg>

    <header class="brand">
      <span class="brand__mark" aria-hidden="true"></span>
      <h1 class="brand__name">Blue Harbor Marketing</h1>
    </header>
  </main>
</body>
</html>
```